Visitenkarten-Design für Stillberaterin
Zielgruppe
Ich bin Stillberaterin ZMRPT, d. h. ich berate Mütter bei Stillschwierigkeiten. Meine Zielgruppe sind junge Familien, die sich vorab über das Stillen Ihres Kindes informieren möchten, Stillschwierigkeiten (z. B. Schmerzen, schlechte Gewichtszunahme usw.) haben oder Fragen rund ums Stillen haben (Medikamente, Stillen in besonderen Situationen...). Weiterhin biete ich Kurse für den Beikoststart oder zum Abstillen an.
Aufgabenstellung
Auf meiner Visitenkarte sollte mein Logo sowie alle Kontaktdaten klar und deutlich erkennbar sein. Die Farben sind dem Logo anzupassen. Die Schriftarten, die im Logo verwendet werden sind: Be Bright und Apple Tree

```html
<!DOCTYPE html>
<html lang="de">
<head>
<meta charset="utf-8">
<title>Visitenkarte Still-Momente</title>
<link href="https://fonts.googleapis.com/css2?family=Dancing+Script:wght@500&family=Didact+Gothic&display=swap" rel="stylesheet">
<style>
  :root {
    --canvas: #d3d4d6;
    --paper: #ffffff;
    --pink: #e8509a;
    --pink-soft: #f6d3df;
    --pink-deep: #e54e98;
    --pink-light: #f2a6b3;
    --ink: #2b2b2b;
    --white: #ffffff;
  }
  * { margin: 0; padding: 0; box-sizing: border-box; }
  html, body { width: 1200px; height: 1200px; overflow: hidden; background: var(--canvas); }
  .sheet { position: relative; width: 1200px; height: 1200px; }

  .card { position: absolute; left: 263px; width: 674px; height: 388px; overflow: hidden; }
  .card--front { top: 169px; background: var(--paper); }
  .card--back {
    top: 641px;
    background: linear-gradient(120deg, var(--pink-deep) 0%, #ef85ab 35%, var(--pink-light) 58%, #f09ab3 75%, #ea6aa2 100%);
  }

  .brand-name { font-family: "Didact Gothic", sans-serif; font-size: 30px; letter-spacing: 0.5px; white-space: nowrap; }
  .card--front .brand-name { position: absolute; left: 40px; top: 118px; width: 190px; text-align: center; color: var(--pink); }

  .decor-hearts {
    position: absolute; border-radius: 50%;
    background: radial-gradient(ellipse at center, rgba(246, 211, 223, 0.55) 0%, rgba(246, 211, 223, 0.25) 55%, rgba(246, 211, 223, 0) 75%);
  }
  .card--front .decor-hearts { left: 22px; top: 213px; width: 196px; height: 150px; }
  .card--back .decor-hearts {
    left: 462px; top: 205px; width: 188px; height: 135px;
    background: radial-gradient(ellipse at center, rgba(255, 235, 240, 0.45) 0%, rgba(255, 235, 240, 0.2) 55%, rgba(255, 235, 240, 0) 75%);
  }

  .flow-line { position: absolute; left: 0; top: 0; width: 674px; height: 388px; }

  .holder-name {
    position: absolute; left: 333px; top: 40px;
    font-family: "Dancing Script", cursive; font-weight: 500; font-size: 50px; color: var(--pink); white-space: nowrap;
  }
  .holder-rule { position: absolute; left: 333px; top: 120px; width: 292px; height: 2px; background: var(--pink); }

  .holder-role {
    position: absolute; left: 372px; top: 166px;
    font-family: "Didact Gothic", sans-serif; font-size: 15px; line-height: 27px; color: var(--ink);
  }
  .contact-list { position: absolute; left: 342px; top: 228px; list-style: none; font-family: "Didact Gothic", sans-serif; font-size: 15px; color: var(--ink); }
  .contact-item { position: relative; padding-left: 30px; line-height: 27px; }
  .contact-item + .contact-item { margin-top: 6px; }
  .contact-icon { position: absolute; left: 0; top: 6px; width: 16px; height: 16px; }

  .frame { position: absolute; left: 15px; top: 15px; right: 15px; bottom: 15px; border: 1.5px solid var(--white); }
  .card--back .brand-name { position: absolute; left: 0; top: 186px; width: 674px; text-align: center; color: var(--white); font-size: 34px; }
  .website {
    position: absolute; left: 0; top: 322px; width: 674px; text-align: center;
    font-family: "Dancing Script", cursive; font-weight: 500; font-size: 27px; color: var(--white);
  }
  .website-flourish { position: absolute; top: 338px; width: 54px; height: 6px; border-radius: 3px; background: rgba(255, 255, 255, 0.55); }
  .website-flourish--left { left: 152px; }
  .website-flourish--right { left: 468px; }
</style>
</head>
<body>
<main class="sheet">

  <section class="card card--front" aria-label="Visitenkarte Vorderseite">
    <div class="decor-hearts" role="img" aria-label="Dekoration: zwei verschlungene Herzen in zartem Rosa"></div>
    <svg class="flow-line" viewBox="0 0 674 388" aria-hidden="true">
      <path d="M0 318 C 90 330, 170 350, 260 340 S 470 300, 674 290" fill="none" stroke="#f3cddb" stroke-width="1.5"/>
    </svg>
    <div class="brand-name">Still-Momente</div>

    <h1 class="holder-name">Marlene Kessler</h1>
    <div class="holder-rule"></div>
    <p class="holder-role">Fachkinderkrankenschwester,<br>Still- &amp; Laktationsberaterin ZMRPT</p>

    <ul class="contact-list">
      <li class="contact-item">
        <svg class="contact-icon" viewBox="0 0 16 16" aria-hidden="true"><path d="M8 15 C 4 10, 3 8, 3 6 A5 5 0 0 1 13 6 C 13 8, 12 10, 8 15 Z" fill="none" stroke="#e8509a" stroke-width="1.3"/><circle cx="8" cy="6" r="1.8" fill="none" stroke="#e8509a" stroke-width="1.3"/></svg>
        Am Lindenhang 4<br>93085 Mooshausen
      </li>
      <li class="contact-item">
        <svg class="contact-icon" viewBox="0 0 16 16" aria-hidden="true"><path d="M3 2 L6 2 L7 5 L5.5 6.5 C 6.5 8.5, 7.5 9.5, 9.5 10.5 L11 9 L14 10 L14 13 C 14 14, 13 14.5, 12 14.3 C 7 13.5, 2.5 9, 1.7 4 C 1.5 3, 2 2, 3 2 Z" fill="none" stroke="#e8509a" stroke-width="1.2" stroke-linejoin="round"/></svg>
        09401 5550123
      </li>
      <li class="contact-item">
        <svg class="contact-icon" viewBox="0 0 16 16" aria-hidden="true"><rect x="1.5" y="3.5" width="13" height="9" fill="none" stroke="#e8509a" stroke-width="1.2"/><path d="M1.5 3.5 L8 9 L14.5 3.5" fill="none" stroke="#e8509a" stroke-width="1.2"/></svg>
        marlene@still-momente.de
      </li>
    </ul>
  </section>

  <section class="card card--back" aria-label="Visitenkarte Rückseite">
    <div class="decor-hearts" role="img" aria-label="Dekoration: zwei verschlungene Herzen in hellem Rosa"></div>
    <svg class="flow-line" viewBox="0 0 674 388" aria-hidden="true">
      <path d="M0 298 C 60 300, 110 320, 200 318 S 400 285, 520 300 S 640 330, 674 320" fill="none" stroke="rgba(255,255,255,0.5)" stroke-width="1.5"/>
    </svg>
    <div class="frame"></div>
    <div class="brand-name">Still-Momente</div>
    <div class="website-flourish website-flourish--left" role="img" aria-label="Zierschnörkel"></div>
    <p class="website">www.still-momente.de</p>
    <div class="website-flourish website-flourish--right" role="img" aria-label="Zierschnörkel"></div>
  </section>

</main>
</body>
</html>
```